We would like to incorporate our logo into letterhead design and envelopes. We are looking for something that is moderately conservative but not old law firm style. Both the envelopes and the letterhead must have both firm addresses. We would like to incorporate the color of the logo, but only a small amount of color - perhaps on one of the borders. The addresses for the firm locations are listed below. Given that it is a law firm, it needs to somewhat conservative, but not the old school, small black font on cream colored paper design.

The firm addresses are:

27815 N. Harlow Pemberton Pkwy.
Ste 4200
Carver Ridge, NM 85391

6100 W. Cedar Avenue
Ste 700
Linden Vale, OR 91623

Industry/Entity Type

Legal

Colors

Designer to choose colors to be used in the design.

Requirements
Must have
• Both addresses:
• 27815 N. Harlow Pemberton Pkwy.
• Ste 4200
• Carver Ridge, NM 85391
• 6100 W. Cedar Avenue
• Ste 700
• Linden Vale, OR 91623
Nice to have
• Small amount of color on border(s) that matches the logo but not too much color

```html
<!DOCTYPE html>
<html lang="en">
<head>
<meta charset="utf-8">
<title>Marlowe Law Stationery</title>
<link rel="stylesheet" href="https://fonts.googleapis.com/css2?family=Poppins:wght@400&display=swap">
<style>
  :root {
    --navy: #231f5c;
    --paper: #e9e6df;
    --paper-warm: #ebe6da;
    --backdrop: #e1e1e1;
    --ink: #1f1f1f;
    --light: #f4f1ea;
  }
  * { margin: 0; padding: 0; box-sizing: border-box; }
  html, body { width: 1200px; height: 882px; overflow: hidden; }
  body {
    position: relative;
    background: var(--backdrop);
    font-family: "Poppins", sans-serif;
    color: var(--ink);
  }
  .sheet { position: absolute; background: var(--paper); }
  address { font-style: normal; }

  .firm-name {
    font-family: "Poppins", sans-serif;
    font-weight: 400;
    color: var(--light);
    letter-spacing: 0.5px;
    white-space: nowrap;
    line-height: 1;
  }

  /* Envelope front */
  .envelope-front { left: 108px; top: 310px; width: 470px; height: 215px; }
  .envelope-front .header-band {
    position: absolute; left: 0; top: 0; width: 100%; height: 66px;
    background: var(--navy);
  }
  .envelope-front .firm-name {
    position: absolute; left: 31px; top: 20px; font-size: 24px;
  }
  .return-address {
    position: absolute; left: 30px; top: 76px;
    font-size: 7.8px; line-height: 9.6px;
  }
  .return-address .office + .office { margin-top: 6px; }
  .footer-band {
    position: absolute; left: 0; bottom: 0; width: 100%; height: 8px;
    background: var(--navy);
  }

  /* Envelope back */
  .envelope-back { left: 107px; top: 565px; width: 472px; height: 217px; background: var(--paper-warm); }
  .envelope-back .flap { position: absolute; left: 0; top: 0; display: block; }
  .envelope-back .firm-name {
    position: absolute; left: 0; width: 100%; top: 28px;
    text-align: center; font-size: 16px;
  }

  /* Letterhead */
  .letterhead { left: 605px; top: 78px; width: 497px; height: 703px; }
  .letterhead .header-band {
    position: absolute; left: 0; top: 0; width: 100%; height: 78px;
    background: var(--navy);
  }
  .letterhead .firm-name {
    position: absolute; left: 0; width: 100%; top: 24px;
    text-align: center; font-size: 27px;
  }
  .letterhead-addresses {
    position: absolute; left: 0; width: 100%; top: 658px;
    text-align: center; font-size: 7.8px; line-height: 12px;
  }
</style>
</head>
<body>

  <section class="sheet envelope-front" aria-label="Envelope front">
    <div class="header-band">
      <div class="firm-name">MARLOWE LAW</div>
    </div>
    <address class="return-address">
      <div class="office">
        27815 N. Harlow Pemberton Pkwy.<br>
        Ste 4200<br>
        Carver Ridge, NM 85391
      </div>
      <div class="office">
        6100 W. Cedar Avenue<br>
        Ste 700<br>
        Linden Vale, OR 91623
      </div>
    </address>
    <div class="footer-band"></div>
  </section>

  <section class="sheet envelope-back" aria-label="Envelope back">
    <svg class="flap" width="472" height="79" viewBox="0 0 472 79" aria-hidden="true">
      <path d="M0 0 H472 L462 48 Q456 79 424 79 H48 Q16 79 10 48 Z" fill="var(--navy)"/>
    </svg>
    <div class="firm-name">MARLOWE LAW</div>
  </section>

  <section class="sheet letterhead" aria-label="Letterhead">
    <div class="header-band">
      <div class="firm-name">MARLOWE LAW</div>
    </div>
    <address class="letterhead-addresses">
      6100 W. Cedar Avenue, Ste 700, Linden Vale, OR 91623<br>
      27815 N. Harlow Pemberton Pkwy., Ste 4200, Carver Ridge, NM 85391
    </address>
    <div class="footer-band"></div>
  </section>

</body>
</html>
```